Medical equipment business looking for professional, unique business card

We need a business card design for a durable medical equipment company. We are small but would like our cards to express that we are much bigger. We focus on braces (back, knee, wrist, etc) but also do crutches, rollators, wheelchairs- basically medical equipment that gets you going and back in Action. Our colors are blue and green and our logo has an arrow and use of a "spine". We'd like to express professionalism while being unique.

Industry/Entity Type

Medical Equipment

Contact Information for Business Card

Professional feel but unique. Memorable.

Font styles to use
Serif
Sans Serif
Other font styles liked:
• verdana

Requirements
Must have
• card holders cell#, business phone#, fax#, email, website address, business address, logo
Nice to have
• use of medical/healthcare related descriptive words, items, look
Should not have
• the wrong colors or cartoon characters.

```html
<!DOCTYPE html>
<html lang="en">
<head>
<meta charset="utf-8">
<title>Corvane DME Business Card</title>
<link rel="stylesheet" href="https://fonts.googleapis.com/css2?family=Open+Sans:wght@400;600;700&display=swap">
<style>
  :root {
    --bg: #ecebe8;
    --card: #ffffff;
    --navy: #0b466c;
    --green: #8dc63f;
    --blue: #1a86c6;
    --ink: #3a3a3a;
  }
  * { margin: 0; padding: 0; box-sizing: border-box; }
  html, body { width: 1200px; height: 1000px; overflow: hidden; }
  body {
    background: var(--bg);
    font-family: "Open Sans", Verdana, sans-serif;
    color: var(--ink);
    position: relative;
  }
  .card {
    position: absolute;
    left: 266px;
    width: 666px;
    height: 397px;
    background: var(--card);
    border-radius: 24px;
    overflow: hidden;
  }
  .card--front { top: 74px; }
  .card--back { top: 533px; }
  .card > * { position: absolute; }
  .wave { left: 0; top: 0; width: 666px; height: 397px; }

  .brand { text-align: right; }
  .brand__name {
    font-size: 46px;
    font-weight: 600;
    color: var(--navy);
    line-height: 1;
    letter-spacing: -0.5px;
    white-space: nowrap;
  }
  .brand__tagline {
    font-size: 15px;
    font-weight: 600;
    color: var(--blue);
    margin-top: 12px;
    white-space: nowrap;
  }
  .card--front .brand { right: 47px; top: 40px; }
  .card--back .brand { right: 34px; top: 40px; }

  .holder { left: 33px; top: 178px; }
  .holder__name { font-size: 21px; font-weight: 700; color: var(--navy); letter-spacing: 0.3px; line-height: 26px; }
  .holder__title { font-size: 16px; color: var(--green); line-height: 22px; }

  .contact { left: 414px; top: 172px; font-size: 16.5px; line-height: 23px; }
  .contact__address { margin-bottom: 10px; }
  .contact__row { display: flex; align-items: center; gap: 8px; line-height: 23px; }
  .contact__icon { width: 14px; height: 14px; flex: none; }

  .website { left: 33px; top: 348px; color: #fff; font-size: 16px; letter-spacing: 0.5px; }

  .appointment { left: 33px; top: 38px; }
  .appointment__title { font-size: 21px; font-weight: 700; color: var(--navy); letter-spacing: 0.3px; }
  .appointment__note { font-size: 16.5px; line-height: 20px; margin-top: 6px; }

  .field {
    left: 33px; width: 601px;
    border-bottom: 2px solid var(--green);
    font-size: 16px; padding-bottom: 1px;
  }
  .field--date { top: 159px; }
  .field--time { top: 203px; }

  .days {
    left: 33px; width: 601px; top: 261px;
    display: flex; justify-content: space-between;
    font-size: 16px;
  }
  .day { display: flex; align-items: center; gap: 10px; }
  .day__box { width: 15px; height: 15px; border: 2px solid var(--navy); display: inline-block; }
</style>
</head>
<body>

<section class="card card--front">
  <svg class="wave" viewBox="0 0 666 397" aria-hidden="true">
    <path fill="var(--navy)" d="M0,336 C150,296 300,306 430,346 C520,372 600,360 666,303 L666,397 L0,397 Z"/>
    <path fill="var(--green)" d="M75,308 C200,296 330,312 432,340 C540,368 612,352 652,316 C606,362 530,372 430,350 C320,322 200,304 75,308 Z"/>
  </svg>
  <div class="brand">
    <div class="brand__name">Corvane DME</div>
    <div class="brand__tagline">Durable Medical Equipment</div>
  </div>
  <div class="holder">
    <div class="holder__name">DANA WHITFIELD</div>
    <div class="holder__title">Managing Director</div>
  </div>
  <div class="contact">
    <div class="contact__address">Post Office Box 4410372<br>Riverton, LA 70412</div>
    <div class="contact__row">
      <svg class="contact__icon" viewBox="0 0 14 14" aria-hidden="true"><rect x="3.5" y="0.5" width="7" height="13" rx="1.5" fill="none" stroke="var(--green)" stroke-width="1.4"/><circle cx="7" cy="11" r="0.9" fill="var(--green)"/></svg>
      <span>+ 000 000 0000 EXT 1</span>
    </div>
    <div class="contact__row">
      <svg class="contact__icon" viewBox="0 0 14 14" aria-hidden="true"><path fill="var(--green)" d="M1,5 C1,2 13,2 13,5 L10,6 L10,4.5 L4,4.5 L4,6 Z M3,7 L11,7 L12,12 L2,12 Z"/></svg>
      <span>+ 000 000 0000 EXT 1</span>
    </div>
    <div class="contact__row">
      <svg class="contact__icon" viewBox="0 0 14 14" aria-hidden="true"><rect x="3.5" y="1" width="7" height="3" fill="var(--green)"/><rect x="1" y="5" width="12" height="5" rx="1" fill="var(--green)"/><rect x="3.5" y="8.5" width="7" height="4.5" fill="#fff" stroke="var(--green)" stroke-width="1.2"/></svg>
      <span>+ 000 000 0000 EXT 1</span>
    </div>
    <div class="contact__row">
      <svg class="contact__icon" viewBox="0 0 14 14" aria-hidden="true"><rect x="1" y="3" width="12" height="9" fill="var(--green)"/><path d="M1,3 L7,8 L13,3" fill="none" stroke="#fff" stroke-width="1.2"/></svg>
      <span>info@CorvaneDME.com</span>
    </div>
  </div>
  <div class="website">www.CorvaneDME.com</div>
</section>

<section class="card card--back">
  <svg class="wave" viewBox="0 0 666 397" aria-hidden="true">
    <path fill="var(--navy)" d="M0,342 C150,300 300,310 430,350 C520,376 600,364 666,306 L666,397 L0,397 Z"/>
    <path fill="var(--green)" d="M75,310 C200,298 330,316 432,344 C540,372 612,356 652,318 C606,366 530,376 430,354 C320,326 200,306 75,310 Z"/>
  </svg>
  <div class="appointment">
    <div class="appointment__title">APPOINTMENT</div>
    <p class="appointment__note">If you are unable to keep<br>your appointment , please allow<br>24 hours notice</p>
  </div>
  <div class="brand">
    <div class="brand__name">Corvane DME</div>
    <div class="brand__tagline">Durable Medical Equipment</div>
  </div>
  <div class="field field--date">Date:</div>
  <div class="field field--time">Time:</div>
  <div class="days">
    <span class="day">MON <i class="day__box"></i></span>
    <span class="day">TUE <i class="day__box"></i></span>
    <span class="day">WED <i class="day__box"></i></span>
    <span class="day">THUR <i class="day__box"></i></span>
    <span class="day">FRI <i class="day__box"></i></span>
    <span class="day">SAT <i class="day__box"></i></span>
  </div>
</section>

</body>
</html>
```